Showroom Quote Web Application - Material Design wanted

This web app is an internal application that will be used by one of our customers to build quotes and produce orders of retail items with their customers

the overall design should use the colour pallet provided and have a clean and simple interface

we'd like to go with a material design type of look

attached mockups are just a rough stab at some layouts to give you an example, please feel free to reach out with any questions.

Please don't get hung up on the specific pages, they were intended to provide context, we are looking for a high level design using the provided colour schemes and fonts, additional work may follow for the selected designer when it comes to specific pages or work flows.

Sorry for the short timeline, we have a tight deadline on this one.

Target Market(s)

internal application for customer

Industry/Entity Type

Retail

Other font styles liked:
• see attached doc for fonts

Requirements
Must have
• simple and clean interface
• intuitive design
Nice to have
• see attached documents for logo colour schemes and fonts
• these must be incorporated into the design

```html
<!DOCTYPE html>
<html lang="en">
<head>
<meta charset="utf-8">
<title>Products – Product Details</title>
<link href="https://fonts.googleapis.com/css2?family=Source+Sans+3:ital,wght@0,300;0,400;0,600;0,700;1,300;1,400&display=swap" rel="stylesheet">
<style>
  :root {
    --navy: #002361;
    --gold: #8b7341;
    --page: #f7f7f7;
    --card: #ffffff;
    --field: #ede8e2;
    --text: #2f2f2f;
    --muted: #9a9a9a;
    --rule: #e4e4e4;
  }
  * { box-sizing: border-box; margin: 0; padding: 0; }
  html, body { width: 1200px; height: 675px; overflow: hidden; }
  body {
    background: var(--page);
    font-family: "Source Sans 3", "Source Sans Pro", sans-serif;
    color: var(--text);
    position: relative;
  }
  .topbar {
    position: absolute; left: 0; top: 0; width: 1200px; height: 53px;
    background: var(--navy); display: flex; align-items: center;
  }
  .brand {
    margin-left: 25px; color: #c9cfdc; font-size: 11.5px; letter-spacing: 1.6px;
    font-weight: 400; width: 113px;
  }
  .nav { display: flex; height: 53px; }
  .nav-item {
    display: flex; align-items: center; gap: 4px; padding: 0 7px; height: 53px;
    color: #fff; font-size: 9.8px; font-weight: 700; text-transform: uppercase;
    margin-right: 4px; border-bottom: 3px solid transparent; padding-top: 3px;
  }
  .nav-item svg { width: 14px; height: 14px; fill: currentColor; }
  .nav-item.is-active { color: var(--gold); border-bottom-color: var(--gold); }
  .topbar-tools { margin-left: auto; display: flex; align-items: center; gap: 26px; margin-right: 26px; }
  .mail-icon { width: 14px; height: 11px; fill: #fff; }
  .avatar {
    width: 37px; height: 37px; border-radius: 50%;
    background: radial-gradient(circle at 50% 40%, #e8c9b3, #8a5a3c 75%);
    border: 2px solid #fff;
  }
  .page-head { position: absolute; left: 26px; top: 94px; }
  .page-title { color: var(--navy); font-size: 21px; font-weight: 400; line-height: 1.1; }
  .page-sub { color: var(--muted); font-size: 10px; margin-top: 2px; }
  .search {
    position: absolute; left: 960px; top: 106px; width: 213px; height: 26px;
    border: 1px solid #dadada; border-radius: 13px; background: #fafafa;
    display: flex; align-items: center; padding: 0 10px;
    font-size: 10px; font-style: italic; color: #777;
  }
  .search svg { margin-left: auto; width: 12px; height: 12px; fill: #b5b5b5; }
  .card {
    position: absolute; left: 26px; top: 145px; width: 1148px; height: 482px;
    background: var(--card); border-radius: 10px;
    box-shadow: 0 1px 6px rgba(0,0,0,0.06);
  }
  .item-title {
    position: absolute; top: 30px; width: 100%; text-align: center;
    color: var(--navy); font-size: 31px; font-weight: 700;
  }
  .tabs {
    position: absolute; left: 21px; right: 21px; top: 76px; height: 22px;
    border-bottom: 2px solid var(--rule); display: flex; justify-content: center; gap: 10px;
  }
  .tab {
    padding: 0 10px; font-size: 11.5px; font-weight: 700; color: var(--muted);
    text-transform: uppercase; height: 22px; border-bottom: 3px solid transparent; margin-bottom: -2px;
  }
  .tab.is-active { color: var(--gold); border-bottom-color: var(--gold); }
  .form-note {
    position: absolute; left: 77px; top: 130px; font-size: 14px; font-style: italic; font-weight: 300;
  }
  .form-grid {
    position: absolute; top: 162px; left: 0; width: 100%;
    display: grid; grid-template-columns: 158px 396px 121px 396px;
    column-gap: 5px; row-gap: 10.5px; padding-left: 0;
  }
  .field-label {
    text-align: right; font-size: 14px; font-weight: 700; line-height: 37px;
  }
  .field-value {
    background: var(--field); height: 37px; line-height: 37px; padding: 0 16px;
    font-size: 14px;
  }
</style>
</head>
<body>
  <header class="topbar">
    <div class="brand">LogoGoesHere</div>
    <nav class="nav">
      <div class="nav-item"><svg viewBox="0 0 16 16"><path d="M8 1 0 8h2v7h4v-5h4v5h4V8h2z"/></svg>Dashboard</div>
      <div class="nav-item"><svg viewBox="0 0 16 16"><circle cx="8" cy="8" r="8"/><path d="M8.7 3v1.2c1.2.2 2 .9 2.1 2H9.5c-.1-.5-.5-.8-1.3-.8-.8 0-1.2.3-1.2.7 0 .5.5.6 1.5.9 1.4.3 2.4.8 2.4 2.1 0 1.1-.9 1.8-2.2 2V13H7.5v-1.2c-1.3-.2-2.2-1-2.3-2.2h1.4c.1.6.6 1 1.5 1 .9 0 1.3-.3 1.3-.8s-.4-.7-1.5-.9c-1.2-.3-2.3-.7-2.3-2 0-1 .8-1.7 2-1.9V3z" fill="#002361"/></svg>Accounting</div>
      <div class="nav-item"><svg viewBox="0 0 18 16"><circle cx="6" cy="4.5" r="3"/><circle cx="12.5" cy="4" r="2.5"/><path d="M0 14c0-3.5 2.7-5.5 6-5.5s6 2 6 5.5zM12.8 8c3 0 5.2 1.8 5.2 5h-5c0-2-.7-3.6-2-4.7.6-.2 1.2-.3 1.8-.3z"/></svg>Customers</div>
      <div class="nav-item is-active"><svg viewBox="0 0 16 16"><path d="M7 0h2l.4 2.1 1.4.6 1.8-1.2 1.4 1.4-1.2 1.8.6 1.4L16 7v2l-2.1.4-.6 1.4 1.2 1.8-1.4 1.4-1.8-1.2-1.4.6L9 16H7l-.4-2.1-1.4-.6-1.8 1.2-1.4-1.4 1.2-1.8-.6-1.4L0 9V7l2.1-.4.6-1.4-1.2-1.8 1.4-1.4 1.8 1.2 1.4-.6zM8 5a3 3 0 1 0 0 6 3 3 0 0 0 0-6z"/></svg>Products</div>
      <div class="nav-item"><svg viewBox="0 0 16 16"><rect y="2" width="16" height="2.4"/><rect y="6.8" width="16" height="2.4"/><rect y="11.6" width="16" height="2.4"/></svg>More</div>
    </nav>
    <div class="topbar-tools">
      <svg class="mail-icon" viewBox="0 0 14 11"><path d="M0 0h14v1.2L7 6 0 1.2zM0 2.8l7 4.8 7-4.8V11H0z"/></svg>
      <div class="avatar" role="img" aria-label="User profile photo"></div>
    </div>
  </header>

  <div class="page-head">
    <h1 class="page-title">Products</h1>
    <p class="page-sub">Product Details</p>
  </div>
  <div class="search">Search products...<svg viewBox="0 0 16 16"><path d="M6.5 0a6.5 6.5 0 0 1 5.2 10.4L16 14.6 14.6 16l-4.2-4.3A6.5 6.5 0 1 1 6.5 0zm0 2.2a4.3 4.3 0 1 0 0 8.6 4.3 4.3 0 0 0 0-8.6z"/></svg></div>

  <main class="card">
    <h2 class="item-title">Item 83MB1130-00</h2>
    <div class="tabs">
      <div class="tab is-active">Main</div>
      <div class="tab">Images</div>
      <div class="tab">Costs</div>
    </div>
    <p class="form-note">Please fill out the new customer's information.</p>
    <div class="form-grid">
      <div class="field-label">WFS #</div><div class="field-value">83MB130-00</div>
      <div class="field-label">Part #</div><div class="field-value">130010007</div>
      <div class="field-label">WFS Desc</div><div class="field-value">VESTA ROUND FRONT 12" ROUGH IN</div>
      <div class="field-label">MFG #</div><div class="field-value">130010007</div>
      <div class="field-label">Vendor Desc</div><div class="field-value">VESTA BOWL 130 ROUND WHITE</div>
      <div class="field-label">Vendor Code</div><div class="field-value">130</div>
      <div class="field-label">MFG</div><div class="field-value">HARLOW</div>
      <div class="field-label">Cost</div><div class="field-value">$123.00</div>
    </div>
  </main>
</body>
</html>
```